Power point design for a financial seminar

I would like to receive 10 designed power point slides with the same look & feel that should related to finance since its for a seminar related to stock markets and economics. Please note that texts are in Hebrew (translate is attached in a Word document).
There should be background with upper and bottom layers similar to all to include the attached logo.
All slides should have a Title and some of the slides should have designed bullets and other generic graphic elements that we will use in our presentation.
Please note that text should be right to left so texts will be aligned to the right and graphics at the left/upper/bottom
Youngsters

```html
<!DOCTYPE html>
<html lang="en">
<head>
<meta charset="utf-8">
<title>The Capital Market Course – Basic</title>
<link href="https://fonts.googleapis.com/css2?family=Poppins:wght@400;500;600;800&family=Roboto:wght@400;500;700&display=swap" rel="stylesheet">
<style>
:root{
  --page:#f2f2f2;
  --white:#ffffff;
  --blue:#0a6bd1;
  --teal:#3fb9b7;
  --teal-light:#a9dedf;
  --yellow:#e0c900;
  --gold:#f2c500;
  --ink:#2b2b2b;
  --arrow:#a8682c;
  --green:#2c9a5a;
  --red:#d23b3b;
  --table-head:#1a3f78;
}
*{box-sizing:border-box;margin:0;padding:0}
html,body{width:1200px;height:3652px;overflow:hidden}
body{background:var(--page);font-family:"Poppins",sans-serif;color:var(--ink);position:relative}
.slide{position:absolute;left:99px;width:1002px;height:563px;background:var(--white);overflow:hidden}
.footer{position:absolute;left:0;bottom:0;width:100%;height:41px;background:var(--teal)}
.footer-mark{position:absolute;left:18px;top:8px;width:25px;height:25px;border:2px solid var(--white);border-radius:50%}
.page-num{position:absolute;right:16px;top:7px;width:27px;height:27px;border-radius:50%;background:#000;color:var(--white);font-size:13px;font-weight:600;line-height:27px;text-align:center}
.corner-brand{position:absolute;left:16px;top:24px;display:flex;align-items:center;gap:6px}
.corner-brand .dot{width:46px;height:46px;border-radius:50%;border:3px solid var(--blue)}
.corner-brand span{font-size:12px;font-weight:600;color:var(--blue)}
.title{position:absolute;right:42px;top:22px;font-weight:800;color:var(--blue);font-size:56px;line-height:1.0;text-align:right}
.photo-circle{position:absolute;border-radius:50%}
.ring{position:absolute;overflow:visible}

/* Cover */
.cover-photo{position:absolute;inset:0;background:radial-gradient(circle at 30% 40%,#2a3e66 0%,#14244a 40%,#070e1e 100%)}
.cover-brand{position:absolute;left:735px;top:150px;display:flex;align-items:center;gap:12px}
.cover-brand .dot{width:80px;height:80px;border-radius:50%;border:5px solid var(--blue)}
.cover-brand span{font-size:26px;font-weight:800;color:var(--gold)}
.cover-title{position:absolute;right:40px;top:330px;text-align:right;color:var(--white);font-weight:800;font-size:41px;line-height:57px}
.cover-name{position:absolute;right:40px;top:461px;color:var(--gold);font-weight:800;font-size:25px}

/* Lecturer */
.badges{position:absolute;left:0;top:186px;width:100%}
.badge{position:absolute;width:190px;text-align:center;top:0}
.badge-disc{position:relative;width:164px;height:164px;margin:0 auto;border-radius:50%;background:var(--yellow);box-shadow:4px 4px 0 0 var(--teal),-2px -2px 0 0 var(--blue)}
.badge-disc svg{position:absolute;left:42px;top:42px;width:80px;height:80px}
.badge p{margin-top:18px;font-size:14px;line-height:21px;color:var(--ink)}

/* Bullets */
.bullets{position:absolute;right:38px;top:110px;list-style:none;text-align:right}
.bullets li{position:relative;padding-right:42px;font-size:19px;line-height:33px;margin-bottom:14px;color:var(--ink)}
.bullets li svg{position:absolute;right:0;top:8px}

/* Assets */
.asset{position:absolute;display:flex;align-items:center;gap:22px}
.asset span{font-size:22px}
.icon-disc{width:78px;height:78px;border-radius:50%;background:var(--teal-light);display:flex;align-items:center;justify-content:center}
.icon-disc svg{width:52px;height:52px}

/* Table */
.index-table{position:absolute;left:391px;top:102px;width:596px;font-family:"Roboto",sans-serif}
.table-head{display:flex;justify-content:space-between;align-items:center;font-size:9px;color:#666;margin-bottom:8px}
.table-tools{display:flex;gap:6px}
.table-head strong{font-size:13px;color:#222;font-weight:700}
table{width:100%;border-collapse:collapse;font-size:10px}
th{font-weight:700;color:var(--table-head);text-align:center;padding:6px 4px 26px;border-bottom:2px solid var(--table-head)}
td{padding:6px 6px;border-bottom:1px solid #e3e3e3;color:#555;text-align:right;height:26px}
td.cat{text-align:center}
td.name{color:var(--blue);text-decoration:underline}
td.up{color:var(--green)}
td.down{color:var(--red)}

/* Features */
.features-label{position:absolute;right:28px;top:160px;color:var(--teal);font-weight:800;font-size:30px}
</style>
</head>
<body>

<!-- Slide 1: Cover -->
<section class="slide" style="top:57px">
  <div class="cover-photo" role="img" aria-label="Photo: woman at trading monitors in an office overlooking a city at night"></div>
  <div class="cover-brand"><div class="dot"></div><span>Velmorix</span></div>
  <h1 class="cover-title">The Capital<br>Market Course – Basic</h1>
  <p class="cover-name">Dana Levran</p>
</section>

<!-- Slide 2: Lecturer Background -->
<section class="slide" style="top:648px">
  <div class="corner-brand"><div class="dot"></div><span>Velmorix</span></div>
  <h2 class="title">Lecturer<br>Background</h2>
  <div class="badges">
    <div class="badge" style="left:6px">
      <div class="badge-disc"><svg viewBox="0 0 80 80" fill="none" stroke="#222" stroke-width="2.5"><rect x="16" y="14" width="40" height="52" rx="3"/><line x1="24" y1="28" x2="48" y2="28"/><line x1="24" y1="36" x2="48" y2="36"/><line x1="24" y1="44" x2="40" y2="44"/><circle cx="56" cy="56" r="9"/><path d="M52 64l-2 10 6-3 6 3-2-10"/></svg></div>
      <p>Holds MBA degree</p>
    </div>
    <div class="badge" style="left:205px">
      <div class="badge-disc"><svg viewBox="0 0 80 80" fill="none" stroke="#222" stroke-width="2.5"><circle cx="28" cy="28" r="8"/><path d="M14 54c0-10 6-16 14-16s14 6 14 16"/><rect x="10" y="54" width="60" height="6"/><rect x="44" y="40" width="22" height="14"/><rect x="42" y="12" width="28" height="18" rx="3"/><line x1="48" y1="19" x2="64" y2="19"/><line x1="48" y1="24" x2="60" y2="24"/></svg></div>
      <p>Lecturer at the Lerin College<br>of Administration</p>
    </div>
    <div class="badge" style="left:404px">
      <div class="badge-disc"><svg viewBox="0 0 80 80" fill="none" stroke="#222" stroke-width="2.5"><circle cx="40" cy="18" r="10"/><path d="M40 12v12M36 15h6a2 2 0 010 4h-4a2 2 0 000 4h6"/><circle cx="40" cy="50" r="7"/><path d="M28 72c0-8 5-13 12-13s12 5 12 13"/><circle cx="16" cy="34" r="6"/><circle cx="64" cy="34" r="6"/><line x1="16" y1="40" x2="16" y2="46"/></svg></div>
      <p>Hi-tech entrepreneur in<br>the field of travel<br>/fintech</p>
    </div>
    <div class="badge" style="left:603px">
      <div class="badge-disc"><svg viewBox="0 0 80 80" fill="none" stroke="#222" stroke-width="2.5"><path d="M10 18h50v40H30l-10 10V58H10z"/><line x1="18" y1="28" x2="46" y2="28"/><line x1="18" y1="34" x2="40" y2="34"/><circle cx="26" cy="46" r="5"/><circle cx="44" cy="46" r="5"/><path d="M58 10l10 10-20 20h-10V30z"/></svg></div>
      <p>Writes opinion columns<br>on economic issues</p>
    </div>
    <div class="badge" style="left:801px">
      <div class="badge-disc"><svg viewBox="0 0 80 80" fill="none" stroke="#222" stroke-width="2.5"><rect x="24" y="8" width="40" height="50" rx="3"/><line x1="32" y1="18" x2="56" y2="18"/><line x1="32" y1="24" x2="50" y2="24"/><rect x="34" y="40" width="5" height="12"/><rect x="43" y="34" width="5" height="18"/><rect x="52" y="28" width="5" height="24"/><path d="M8 62c10-4 18 0 26 4h24l-4 8H20"/></svg></div>
      <p>Founded and<br>managed a company<br>for trading in financial<br>derivatives.</p>
    </div>
  </div>
  <div class="footer"><div class="footer-mark"></div><div class="page-num">2</div></div>
</section>

<!-- Slide 3: Stock Market -->
<section class="slide" style="top:1244px">
  <div class="corner-brand"><div class="dot"></div><span>Velmorix</span></div>
  <h2 class="title" style="top:30px">Stock Market</h2>
  <div class="photo-circle" style="left:37px;top:90px;width:386px;height:386px;background:radial-gradient(circle at 50% 45%,#1b3d4f 0%,#2a6a7c 45%,#8fb7bf 100%)" role="img" aria-label="Photo: hand holding a smartphone showing a stock chart"></div>
  <svg class="ring" style="left:16px;top:69px" width="428" height="428" viewBox="0 0 428 428" fill="none"><path d="M214 8a206 206 0 0 1 0 412" stroke="var(--blue)" stroke-width="9"/><path d="M214 420a206 206 0 0 1-198-150" stroke="var(--teal)" stroke-width="7"/><path d="M16 158A206 206 0 0 1 214 8" stroke="var(--blue)" stroke-width="5"/></svg>
  <ul class="bullets" style="top:104px">
    <li>What is a stock market?<svg width="18" height="14" viewBox="0 0 18 14"><path d="M17 7H2M7 1L1 7l6 6" stroke="var(--arrow)" stroke-width="2.5" fill="none"/></svg></li>
    <li>History of the stock market<svg width="18" height="14" viewBox="0 0 18 14"><path d="M17 7H2M7 1L1 7l6 6" stroke="var(--arrow)" stroke-width="2.5" fill="none"/></svg></li>
    <li>Public companies and issues<svg width="18" height="14" viewBox="0 0 18 14"><path d="M17 7H2M7 1L1 7l6 6" stroke="var(--arrow)" stroke-width="2.5" fill="none"/></svg></li>
    <li>The difference between primary market and<br>secondary market<svg width="18" height="14" viewBox="0 0 18 14"><path d="M17 7H2M7 1L1 7l6 6" stroke="var(--arrow)" stroke-width="2.5" fill="none"/></svg></li>
    <li>How does the stock market affect the economy?<svg width="18" height="14" viewBox="0 0 18 14"><path d="M17 7H2M7 1L1 7l6 6" stroke="var(--arrow)" stroke-width="2.5" fill="none"/></svg></li>
    <li>The Harbor City Exchange HCX versus the<br>Coastline Stock Exchange CSE<svg width="18" height="14" viewBox="0 0 18 14"><path d="M17 7H2M7 1L1 7l6 6" stroke="var(--arrow)" stroke-width="2.5" fill="none"/></svg></li>
    <li>Stages of trading in the Coastline Stock Exchange<svg width="18" height="14" viewBox="0 0 18 14"><path d="M17 7H2M7 1L1 7l6 6" stroke="var(--arrow)" stroke-width="2.5" fill="none"/></svg></li>
  </ul>
  <div class="footer"><div class="footer-mark"></div><div class="page-num">3</div></div>
</section>

<!-- Slide 4: Assets Traded -->
<section class="slide" style="top:1839px">
  <div class="corner-brand"><div class="dot"></div><span>Velmorix</span></div>
  <h2 class="title" style="top:34px">Assets Traded</h2>
  <div class="photo-circle" style="left:37px;top:90px;width:386px;height:386px;background:radial-gradient(circle at 50% 45%,#4f86b5 0%,#2a5a8a 50%,#a9cde6 100%)" role="img" aria-label="Photo: hand touching a tablet with floating financial charts"></div>
  <svg class="ring" style="left:16px;top:69px" width="428" height="428" viewBox="0 0 428 428" fill="none"><path d="M214 8a206 206 0 0 1 0 412" stroke="var(--blue)" stroke-width="9"/><path d="M214 420a206 206 0 0 1-198-150" stroke="var(--teal)" stroke-width="7"/><path d="M16 158A206 206 0 0 1 214 8" stroke="var(--blue)" stroke-width="5"/></svg>
  <div class="asset" style="right:350px;top:166px"><span>Stock</span><div class="icon-disc"><svg viewBox="0 0 52 52" fill="none" stroke="#222" stroke-width="2"><rect x="6" y="8" width="40" height="28"/><line x1="14" y1="14" x2="14" y2="30"/><rect x="11" y="18" width="6" height="8"/><line x1="26" y1="12" x2="26" y2="28"/><rect x="23" y="15" width="6" height="9"/><line x1="38" y1="14" x2="38" y2="32"/><rect x="35" y="18" width="6" height="10"/><path d="M20 36v8h12v-8M16 44h20"/></svg></div></div>
  <div class="asset" style="right:36px;top:166px"><span>Bonds</span><div class="icon-disc"><svg viewBox="0 0 52 52" fill="none" stroke="#222" stroke-width="2"><rect x="6" y="8" width="40" height="22"/><text x="10" y="24" font-size="12" fill="#222" stroke="none" font-family="Poppins,sans-serif">$</text><line x1="22" y1="15" x2="40" y2="15"/><line x1="22" y1="21" x2="40" y2="21"/><circle cx="26" cy="36" r="7"/><path d="M22 42l-2 8 6-3 6 3-2-8"/></svg></div></div>
  <div class="asset" style="right:350px;top:268px"><span>ETFs</span><div class="icon-disc"><svg viewBox="0 0 52 52" fill="none" stroke="#222" stroke-width="2"><circle cx="13" cy="16" r="7"/><rect x="10" y="30" width="6" height="16"/><rect x="20" y="24" width="6" height="22"/><rect x="30" y="28" width="6" height="18"/><circle cx="40" cy="40" r="7"/><path d="M18 22l10-10 6 4 10-10"/></svg></div></div>
  <div class="asset" style="right:36px;top:268px"><span>Mutual Funds</span><div class="icon-disc"><svg viewBox="0 0 52 52" fill="none" stroke="#222" stroke-width="2"><circle cx="26" cy="26" r="8"/><text x="22" y="30" font-size="11" fill="#222" stroke="none" font-family="Poppins,sans-serif">$</text><path d="M14 14a17 17 0 0 1 24 0M38 38a17 17 0 0 1-24 0M8 22l6-8 6 6M44 30l-6 8-6-6"/></svg></div></div>
  <div class="asset" style="right:36px;top:370px"><span>Financial Derivatives</span><div class="icon-disc"><svg viewBox="0 0 52 52" fill="none" stroke="#222" stroke-width="2"><rect x="16" y="6" width="28" height="38" rx="2"/><circle cx="14" cy="18" r="8"/><text x="10" y="22" font-size="11" fill="#222" stroke="none" font-family="Poppins,sans-serif">$</text><rect x="22" y="26" width="4" height="8"/><rect x="28" y="22" width="4" height="12"/><rect x="34" y="18" width="4" height="16"/><line x1="22" y1="38" x2="38" y2="38"/></svg></div></div>
  <div class="footer"><div class="footer-mark"></div><div class="page-num">4</div></div>
</section>

<!-- Slide 5: Indexes -->
<section class="slide" style="top:2438px">
  <div class="corner-brand"><div class="dot"></div><span>Velmorix</span></div>
  <h2 class="title" style="top:26px">Indexes</h2>
  <div class="photo-circle" style="left:23px;top:126px;width:322px;height:322px;background:radial-gradient(circle at 50% 45%,#1e4668 0%,#123150 50%,#4a85a8 100%)" role="img" aria-label="Photo: analyst looking at multiple trading screens"></div>
  <svg class="ring" style="left:13px;top:114px" width="346" height="346" viewBox="0 0 346 346" fill="none"><path d="M173 6a167 167 0 0 1 0 334" stroke="var(--blue)" stroke-width="7"/><path d="M173 340a167 167 0 0 1-160-120" stroke="var(--teal)" stroke-width="6"/><path d="M13 126A167 167 0 0 1 173 6" stroke="var(--blue)" stroke-width="4"/></svg>
  <div class="index-table">
    <div class="table-head">
      <span class="table-tools">
        <svg width="12" height="12" viewBox="0 0 12 12" fill="none" stroke="#777" stroke-width="1.2"><path d="M6 1v7M3 5l3 3 3-3M1 10h10"/></svg>
        <svg width="12" height="12" viewBox="0 0 12 12" fill="none" stroke="#777" stroke-width="1.2"><rect x="3" y="1" width="6" height="3"/><rect x="1" y="4" width="10" height="5"/><rect x="3" y="7" width="6" height="4"/></svg>
      </span>
      <span>A total of 89 records | As of <b>09/19/2023 11:37</b> &nbsp;<strong>Index trading data</strong></span>
    </div>
    <table>
      <thead><tr><th>last update</th><th>(%) change</th><th>last gate</th><th>Index code</th><th>category</th><th style="text-align:right">Name</th></tr></thead>
      <tbody>
        <tr><td>11:37</td><td class="up">0.06%</td><td>357.71</td><td>722</td><td class="cat">Bond indices</td><td class="name">Bond Ladder 3-5</td></tr>
        <tr><td>11:37</td><td class="up">0.07%</td><td>371.53</td><td>723</td><td class="cat">Bond indices</td><td class="name">Bond Ladder 5-15</td></tr>
        <tr><td>11:37</td><td class="up">0.05%</td><td>855.53</td><td>149</td><td class="cat">Branch indices</td><td class="name">CX Real Estate</td></tr>
        <tr><td>11:37</td><td class="up">0.08%</td><td>1,257.99</td><td>181</td><td class="cat">Branch indices</td><td class="name">CX Construction</td></tr>
        <tr><td>11:37</td><td class="up">0.16%</td><td>2,808.71</td><td>033</td><td class="cat">Branch indices</td><td class="name">CX Insurance</td></tr>
        <tr><td>11:37</td><td class="up">0.88%</td><td>1,070.85</td><td>188</td><td class="cat">Branch indices</td><td class="name">CX Retail Networks</td></tr>
        <tr><td>11:37</td><td class="up">0.65%</td><td>2,221.17</td><td>179</td><td class="cat">special measures</td><td class="name">CX Family</td></tr>
        <tr><td>11:37</td><td class="up">0.19%</td><td>2,629.85</td><td>166</td><td class="cat">special measures</td><td class="name">CX Dividend</td></tr>
        <tr><td>11:37</td><td class="up">0.25%</td><td>2,245.82</td><td>150</td><td class="cat">special measures</td><td class="name">CX Upward</td></tr>
        <tr><td>11:37</td><td class="down">-0.13%</td><td>523.7</td><td>187</td><td class="cat">special measures</td><td class="name">CX Dual</td></tr>
        <tr><td>11:37</td><td class="down">-4.53%</td><td>15.16</td><td>598</td><td class="cat">Derivative indices</td><td class="name">VCX35</td></tr>
      </tbody>
    </table>
  </div>
  <div class="footer"><div class="footer-mark"></div><div class="page-num">5</div></div>
</section>

<!-- Slide 6: Derivatives -->
<section class="slide" style="top:3036px">
  <div class="corner-brand"><div class="dot"></div><span>Velmorix</span></div>
  <h2 class="title" style="top:30px;right:28px">Derivatives</h2>
  <p class="features-label">Features</p>
  <div class="photo-circle" style="left:37px;top:90px;width:386px;height:386px;background:radial-gradient(circle at 50% 45%,#c9a98a 0%,#8c6a52 50%,#d9cbbd 100%)" role="img" aria-label="Photo: business people talking across a table"></div>
  <svg class="ring" style="left:16px;top:69px" width="428" height="428" viewBox="0 0 428 428" fill="none"><path d="M214 8a206 206 0 0 1 0 412" stroke="var(--blue)" stroke-width="9"/><path d="M214 420a206 206 0 0 1-198-150" stroke="var(--teal)" stroke-width="7"/><path d="M16 158A206 206 0 0 1 214 8" stroke="var(--blue)" stroke-width="5"/></svg>
  <div class="asset" style="right:308px;top:214px"><span>Perspiciatis</span><div class="icon-disc"><svg viewBox="0 0 52 52" fill="none" stroke="#222" stroke-width="2"><rect x="8" y="6" width="30" height="40"/><text x="12" y="20" font-size="11" fill="#222" stroke="none" font-family="Poppins,sans-serif">$</text><line x1="22" y1="12" x2="34" y2="12"/><line x1="22" y1="18" x2="34" y2="18"/><rect x="16" y="32" width="4" height="8"/><rect x="24" y="28" width="4" height="12"/><rect x="32" y="24" width="4" height="16"/></svg></div></div>
  <div class="asset" style="right:28px;top:214px"><span>Nemoenim</span><div class="icon-disc"><svg viewBox="0 0 52 52" fill="none" stroke="#222" stroke-width="2"><rect x="6" y="8" width="10" height="10"/><rect x="6" y="21" width="10" height="10"/><rect x="6" y="34" width="10" height="10"/><path d="M16 10h26l4 3-4 3H16M16 23h26l4 3-4 3H16M16 36h26l4 3-4 3H16"/></svg></div></div>
  <div class="asset" style="right:308px;top:318px"><span>Nemoenim</span><div class="icon-disc"><svg viewBox="0 0 52 52" fill="none" stroke="#222" stroke-width="2"><rect x="6" y="8" width="26" height="30"/><path d="M10 30l6-8 5 4 8-12"/><circle cx="38" cy="22" r="6"/><path d="M28 46c0-8 4-12 10-12s10 4 10 12"/><circle cx="12" cy="42" r="6"/></svg></div></div>
  <div class="asset" style="right:28px;top:318px"><span>Corporis</span><div class="icon-disc"><svg viewBox="0 0 52 52" fill="none" stroke="#222" stroke-width="2"><circle cx="26" cy="32" r="12"/><text x="22" y="37" font-size="13" fill="#222" stroke="none" font-family="Poppins,sans-serif">$</text><rect x="4" y="8" width="14" height="10"/><rect x="34" y="8" width="14" height="10"/><rect x="19" y="4" width="14" height="10"/><path d="M11 18v6M41 18v6M26 14v6"/></svg></div></div>
  <div class="asset" style="right:308px;top:420px"><span>Aperiam</span><div class="icon-disc"><svg viewBox="0 0 52 52" fill="none" stroke="#222" stroke-width="2"><rect x="18" y="4" width="24" height="30"/><text x="26" y="18" font-size="11" fill="#222" stroke="none" font-family="Poppins,sans-serif">$</text><rect x="4" y="26" width="18" height="22"/><circle cx="9" cy="33" r="1.5"/><circle cx="17" cy="33" r="1.5"/><circle cx="9" cy="41" r="1.5"/><circle cx="17" cy="41" r="1.5"/><ellipse cx="38" cy="40" rx="8" ry="3"/><ellipse cx="38" cy="45" rx="8" ry="3"/></svg></div></div>
  <div class="footer"><div class="footer-mark"></div><div class="page-num">6</div></div>
</section>

</body>
</html>
```